Marrowind Labs - pioneers of next generation consulting!

We are a next generation management consulting firm with two focus areas and USPs (unique selling points):>Technology driven business developmentWe are not developers, we are experts in HOW to apply and incorporate technology in your business dna to drive business growth and value-added change.>Creating high performing teams levering our philosophy of collective intelligence. We truly understand the need of human engagement and we know that the only way of getting there is by building strong relationships among people, a warm and open culture is a stepping stone towards effective collaboration within/among teams. - We don't want a ”corporate feel” to our templates. The organic feeling we have with our blue-on-blue blobs has the idea of ever changing movement and shape changing. Please see our website, www.marrowindlabs.se. - In our context we sit among classic business mgmt. consultants and classic IT mgmt. consultants. We cater to business, tech and humans as the ultimate vehicle of change and business value. -To have a clean template one suggestion is to only use blue, white and black and keeping other colors separate, as an alternative but we are truly open allow your creativity add value to this. We are looking to find a slide deck which we can pick slides from, depending on what/whom/why we interact with customer we want to create different outcomes and our presentations should support this.

Industry/Entity Type

Management Consulting

Requirements
Must have
• next generation powerpoint and how to package storytelling. please keep to our look and feel, we just arrived at our logo, colours and shapes. Help us to carry it into our ppt's as well.
Should not have
• Hi all, please have a look at our website. It is still very new and more will be done, but our goal is to make powerpoint to come alive again and mirror our pioneering hearts and brains.

```html
<!DOCTYPE html>
<html lang="en">
<head>
<meta charset="utf-8">
<title>Marrowind Labs – Slide Deck Overview</title>
<link href="https://fonts.googleapis.com/css2?family=Open+Sans:wght@400;600;700&family=Permanent+Marker&family=IBM+Plex+Mono:wght@300;400&display=swap" rel="stylesheet">
<style>
:root{
  --navy:#1c3f78;
  --navy-deep:#173569;
  --blue:#2a63c9;
  --blue-mid:#2456b0;
  --blue-light:#a9c2ea;
  --ice:#dfe8f6;
  --white:#ffffff;
  --ink:#1b1b1b;
  --grey:#e6e8ec;
  --slate:#2b3440;
  --red:#b8454a;
}
*{margin:0;padding:0;box-sizing:border-box}
html,body{width:1200px;height:730px;overflow:hidden;background:var(--white)}
body{position:relative;font-family:"Open Sans",sans-serif;color:var(--ink)}
.slide{position:absolute;width:386px;height:217px;overflow:hidden;background:var(--white)}
.col1{left:24px}.col2{left:410px}.col3{left:802px}
.row1{top:16px}.row2{top:256px}.row3{top:491px}
.dark{background:var(--navy);color:var(--white)}
.bright{background:var(--blue);color:var(--white)}
.photo{position:absolute}
.brush{font-family:"Permanent Marker",cursive;text-transform:uppercase;letter-spacing:1px}
.mono{font-family:"IBM Plex Mono",monospace}
.small{font-size:4.3px;line-height:7px}
.wave{position:absolute;left:0;bottom:0;width:386px;height:20px}
.logo-text{position:absolute;right:6px;bottom:3px;font-family:"Open Sans",sans-serif;font-weight:700;font-size:8.5px;letter-spacing:.5px;color:var(--white);text-transform:uppercase}
.page-mark{position:absolute;left:6px;bottom:6px;width:8px;height:1px;background:var(--blue)}
.dark .page-mark,.bright .page-mark{background:var(--white)}
.abs{position:absolute}
</style>
</head>
<body>

<!-- Slide 1: intro collage -->
<section class="slide col1 row1">
  <div class="abs" style="left:18px;top:8px;width:169px;height:96px;background:var(--navy);color:var(--white);text-align:center">
    <div style="margin-top:10px;font-weight:700;font-size:11px;letter-spacing:.5px">MARROWIND LABS</div>
    <div style="margin-top:30px;font-size:7.5px">Future optimism</div>
    <div class="mono" style="font-size:4px;margin-top:3px">We believe in and feel confident about the future</div>
  </div>
  <div class="photo" role="img" aria-label="Hand holding a phone in front of an open fridge" style="left:189px;top:8px;width:165px;height:96px;background:linear-gradient(135deg,#d9d4c4,#8ea07a,#d6c8a8)"></div>
  <div class="photo" role="img" aria-label="People working at a laptop" style="left:18px;top:106px;width:87px;height:50px;background:linear-gradient(135deg,#c9b8a2,#6b625a)"></div>
  <div class="photo" role="img" aria-label="Person wearing a VR headset" style="left:18px;top:158px;width:87px;height:50px;background:linear-gradient(135deg,#3d3d3d,#8a8a8a)"></div>
  <div class="photo" role="img" aria-label="Circuit board close-up" style="left:107px;top:106px;width:80px;height:102px;background:linear-gradient(135deg,#2e5a3c,#9aa08e,#3b4a3a)"></div>
  <div class="photo" role="img" aria-label="Small white service robot" style="left:189px;top:106px;width:80px;height:50px;background:linear-gradient(135deg,#f1f1f1,#b6b6b6)"></div>
  <div class="photo" role="img" aria-label="Engineer at computer screens" style="left:189px;top:158px;width:80px;height:50px;background:linear-gradient(135deg,#5a6470,#c4c8cc)"></div>
  <div class="photo" role="img" aria-label="Face recognition mesh on blue portrait" style="left:271px;top:106px;width:83px;height:102px;background:linear-gradient(135deg,#7fc7e8,#2f86c8,#1c3f78)"></div>
  <span class="page-mark"></span>
</section>

<!-- Slide 2: culture -->
<section class="slide col2 row1">
  <div class="photo" role="img" aria-label="Woman with red hair, toned red" style="left:11px;top:14px;width:138px;height:186px;border-radius:0 0 0 40px;background:linear-gradient(160deg,#c25a55,#9c3236 60%,#7a2a2e)"></div>
  <div class="abs brush" style="left:26px;top:22px;font-size:12px;color:var(--white)">Culture</div>
  <div class="abs mono" style="left:58px;top:38px;font-size:5px;color:var(--white);line-height:6px">Image concept:<br>Human Integration</div>
  <p class="abs" style="left:26px;top:68px;width:120px;font-size:4.6px;line-height:7.6px;color:var(--white);font-weight:600">A wonderful serenity has taken possession of my entire soul, like these sweet mornings of spring which I enjoy with my whole heart. I am alone, and feel the charm of existence in this spot, which was created for the bliss of souls like mine. I am so happy, my dear friend, so absorbed in the exquisite sense of mere tranquil existence, that I neglect my talents.</p>
  <div class="photo" role="img" aria-label="Team workshop at a whiteboard" style="left:155px;top:16px;width:140px;height:60px;background:linear-gradient(135deg,#e9e4de,#a89a8c)"></div>
  <div class="photo" role="img" aria-label="Colleague working at a laptop" style="left:297px;top:16px;width:69px;height:124px;background:linear-gradient(135deg,#5a4a3c,#2a6a4a,#c9b6a0)"></div>
  <div class="photo" role="img" aria-label="Office kitchen gathering" style="left:155px;top:78px;width:69px;height:62px;background:linear-gradient(135deg,#6a4a30,#c8a070)"></div>
  <div class="photo" role="img" aria-label="Group of colleagues smiling" style="left:226px;top:78px;width:69px;height:62px;background:linear-gradient(135deg,#4a5a4a,#a0907a)"></div>
  <div class="photo" role="img" aria-label="Colleagues talking in the office" style="left:155px;top:142px;width:69px;height:60px;background:linear-gradient(135deg,#3a3a3a,#a08a70)"></div>
  <div class="photo" role="img" aria-label="Rooster in a bright office" style="left:226px;top:142px;width:69px;height:60px;background:linear-gradient(135deg,#f0ece6,#b05a2a)"></div>
  <div class="photo" role="img" aria-label="Tattooed hands typing on a laptop" style="left:297px;top:142px;width:69px;height:60px;background:linear-gradient(135deg,#d8d8d8,#707070)"></div>
  <svg class="wave" viewBox="0 0 386 20" aria-hidden="true"><path d="M0 18 C120 16 260 8 386 4 L386 20 L0 20Z" fill="var(--blue-mid)"/></svg>
  <span class="logo-text">Marrowind Labs</span>
  <span class="page-mark"></span>
</section>

<!-- Slide 3: quote blob -->
<section class="slide col3 row1 dark">
  <svg class="abs" style="left:0;top:0" width="386" height="217" viewBox="0 0 386 217" aria-hidden="true">
    <path d="M40 30 C90 -10 190 0 195 40 C200 90 160 175 120 180 C70 186 -10 120 10 80 C18 60 25 42 40 30Z" fill="var(--blue-mid)"/>
    <path d="M52 44 C95 14 170 20 175 52 C180 92 148 160 118 162 C78 165 16 112 30 84 C36 68 42 54 52 44Z" fill="var(--navy)"/>
    <path d="M0 210 C140 212 260 204 386 190 L386 217 L0 217Z" fill="var(--blue-mid)"/>
  </svg>
  <div class="abs brush" style="left:56px;top:74px;font-size:13px;line-height:22px">"Different,<br>&nbsp;&nbsp;sometimes<br>&nbsp;is good"</div>
  <div class="abs mono" style="left:236px;top:74px;font-size:16px;font-weight:300;line-height:22px;letter-spacing:1px">Moving<br>Forward</div>
  <p class="abs small" style="left:236px;top:122px;width:100px;font-size:3.8px;line-height:8px">Common vocabulary keeps us aligned. Clear words make every change easier to share and adopt.</p>
  <span class="logo-text">Marrowind Labs</span>
  <span class="page-mark"></span>
</section>

<!-- Slide 4: smart image -->
<section class="slide col1 row2">
  <div class="abs mono" style="left:42px;top:84px;font-size:5.5px;letter-spacing:2px">SMART IMAGE</div>
  <div class="abs" style="left:42px;top:98px;font-weight:700;font-size:17px;color:var(--navy);line-height:22px">MARROWIND<br>LABS</div>
  <svg class="abs" style="left:182px;top:0" width="204" height="217" viewBox="0 0 204 217" role="img" aria-label="Bright blue corridor with glowing light panels">
    <defs>
      <radialGradient id="corridor" cx=".5" cy=".55" r=".6">
        <stop offset="0" stop-color="#1c3f78"/>
        <stop offset=".35" stop-color="#7fa4d8"/>
        <stop offset="1" stop-color="#e6eefa"/>
      </radialGradient>
    </defs>
    <path d="M20 0 L204 0 L204 217 L10 217 C0 180 25 150 18 110 C10 70 30 40 20 0Z" fill="url(#corridor)"/>
  </svg>
  <span class="page-mark"></span>
</section>

<!-- Slide 5: culture 2.0 -->
<section class="slide col2 row2">
  <div class="photo" role="img" aria-label="Black and white café interior" style="left:10px;top:8px;width:90px;height:100px;background:linear-gradient(135deg,#f2f2f2,#8a8a8a,#2a2a2a)"></div>
  <div class="photo" role="img" aria-label="Black and white street scene" style="left:104px;top:8px;width:90px;height:100px;background:linear-gradient(135deg,#1a1a1a,#777,#222)"></div>
  <div class="abs mono" style="left:208px;top:28px;font-size:4.5px;letter-spacing:2px">SMART TEXT</div>
  <div class="abs brush" style="left:208px;top:38px;font-size:13px;color:var(--navy)">Culture 2.0</div>
  <p class="abs small" style="left:208px;top:62px;width:156px"><b>A wonderful serenity</b> has taken possession of my entire soul, like these sweet mornings of spring which I enjoy with my whole heart. I am alone, and feel the charm of existence in this spot, which was created for the bliss of souls like mine.</p>
  <div class="photo" role="img" aria-label="Blue-toned office with laptop by the window" style="left:193px;top:110px;width:186px;height:107px;background:linear-gradient(135deg,#9ec0ee,#2a63c9,#173569)"></div>
  <div class="abs" style="left:33px;top:132px;width:173px;height:56px;background:var(--blue);color:var(--white);padding:10px 14px">
    <div class="brush" style="position:absolute;top:-4px;left:16px;font-size:14px;color:var(--navy)">"</div>
    <p class="mono" style="font-size:5.3px;line-height:10px;font-style:italic">When, while the lovely valley teems with vapour around me, and the meridian sun strikes the upper surface of the impenetrable.</p>
  </div>
  <svg class="wave" viewBox="0 0 386 20" aria-hidden="true"><path d="M0 18 C120 16 260 8 386 4 L386 20 L0 20Z" fill="var(--blue-mid)"/></svg>
  <span class="logo-text">Marrowind Labs</span>
  <span class="page-mark"></span>
</section>

<!-- Slide 6: testimonial -->
<section class="slide col3 row2 bright">
  <svg class="abs" style="left:0;top:0" width="386" height="217" viewBox="0 0 386 217" aria-hidden="true">
    <path d="M92 48 C130 30 165 60 158 100 C152 140 110 140 90 134 C60 126 58 64 92 48Z" fill="var(--white)"/>
    <path d="M0 170 C120 168 260 150 386 136 L386 217 L0 217Z" fill="var(--navy)"/>
  </svg>
  <div class="photo" role="img" aria-label="Portrait of a senior consultant in black" style="left:98px;top:38px;width:50px;height:96px;border-radius:24px 24px 8px 8px;background:linear-gradient(180deg,#d9b98a,#2a2a2a 45%,#1a1a1a)"></div>
  <p class="abs" style="left:190px;top:54px;width:116px;font-size:4.8px;line-height:7.4px">"Ironically, at a time when the need for consulting done right has never been greater, the consulting industry itself has become lazy, complacent and cynical."</p>
  <div class="abs mono" style="left:190px;top:94px;font-size:4.2px;font-weight:400">Lena Marsh</div>
  <div class="abs mono" style="left:190px;top:100px;font-size:3.8px;color:var(--blue-light)">Senior Management Consultant</div>
  <div class="abs brush" style="left:24px;top:170px;font-size:9.5px;line-height:15px">"Next generation<br>consulting"</div>
  <span class="logo-text">Marrowind Labs</span>
  <span class="page-mark"></span>
</section>

<!-- Slide 7: everywhere -->
<section class="slide col1 row3">
  <div class="photo" role="img" aria-label="Soft blurred blue abstract photograph" style="left:22px;top:37px;width:168px;height:130px;background:linear-gradient(180deg,#8aa4dc,#c8d6f0 45%,#7e9ad8)"></div>
  <div class="abs mono" style="left:18px;top:59px;width:174px;height:80px;background:#f3f3f5;box-shadow:0 2px 8px rgba(0,0,0,.12);padding:16px 14px;font-size:9.5px;line-height:12px;color:#2a2a2a">''A fast-growing company creating the next generation consulting''</div>
  <div class="abs" style="left:226px;top:61px;font-size:5px">Field Notes</div>
  <div class="abs brush" style="left:226px;top:70px;font-size:11px;color:var(--navy)">Everywhere</div>
  <p class="abs small" style="left:226px;top:92px;width:128px;font-size:4px;line-height:6.2px">We apply our passion in business development to create extraordinary results. With research-based philosophy and a fearlessness of evolving technology we champion complex problems to create sustainable results. Do you want to make a difference? Join us if you have the courage to pioneer into the next generation of business development where people and technology co-create a new way forward, a new tomorrow.</p>
  <svg class="wave" viewBox="0 0 386 20" aria-hidden="true"><path d="M0 18 C120 16 260 8 386 4 L386 20 L0 20Z" fill="var(--blue-mid)"/></svg>
  <span class="logo-text">Marrowind Labs</span>
  <span class="page-mark"></span>
</section>

<!-- Slide 8: our consultants -->
<section class="slide col2 row3 dark">
  <svg class="abs" style="left:0;top:0" width="386" height="217" viewBox="0 0 386 217" role="img" aria-label="Consultant presenting to a group, framed in a blue blob">
    <path d="M30 40 C70 20 170 18 180 50 C192 92 150 175 110 178 C70 180 10 120 18 80 C20 62 22 48 30 40Z" fill="var(--blue-mid)"/>
    <defs><linearGradient id="meet" x1="0" y1="0" x2="1" y2="1"><stop offset="0" stop-color="#e6dccf"/><stop offset=".5" stop-color="#8c6e58"/><stop offset="1" stop-color="#3a3a3a"/></linearGradient></defs>
    <path d="M46 54 C80 40 156 40 164 62 C172 96 140 160 110 162 C78 164 30 116 36 86 C38 72 40 60 46 54Z" fill="url(#meet)"/>
  </svg>
  <div class="abs brush" style="left:206px;top:44px;font-size:10.5px">Our consultants</div>
  <div class="abs mono" style="left:206px;top:92px;font-size:7px">Meet Name</div>
  <p class="abs small" style="left:206px;top:104px;width:150px;font-size:4px;line-height:10px">Our team shares one language and one goal: lasting change, built together with clients, teams and people.</p>
  <div class="abs" style="left:206px;top:150px;font-size:3.8px;line-height:7px">Henrik Solberg<br><b>Assistant Manager</b></div>
  <svg class="wave" viewBox="0 0 386 20" aria-hidden="true"><path d="M0 18 C120 16 260 8 386 4 L386 20 L0 20Z" fill="var(--blue-mid)"/></svg>
  <span class="logo-text">Marrowind Labs</span>
  <span class="page-mark"></span>
</section>

<!-- Slide 9: section divider -->
<section class="slide col3 row3" style="background:var(--grey)">
  <div class="abs" style="left:0;top:108px;width:386px;height:109px;background:var(--navy)"></div>
  <div class="photo" role="img" aria-label="Dim office scene behind a dark overlay" style="left:49px;top:46px;width:289px;height:122px;background:linear-gradient(135deg,#3b4450,#2b3440 60%,#40505e);box-shadow:0 2px 8px rgba(0,0,0,.25)"></div>
  <div class="abs brush" style="left:78px;top:66px;font-size:14px;color:var(--blue)">"</div>
  <p class="abs" style="left:78px;top:86px;width:210px;font-size:5.2px;line-height:10px;color:#e8e8e8">The goal of <b>education</b> is not to increase the amount of <b>knowledge</b> but to create the possibilities for a child to <b>invent and discover</b>, to create men who are <b>capable</b> of doing new things.</p>
  <div class="abs" style="left:78px;top:127px;font-size:3.6px;color:#c8c8c8">- Ada Lindqvist</div>
  <div class="abs mono" style="left:198px;top:128px;font-size:32px;font-weight:300;color:var(--white);letter-spacing:2px">01.02</div>
  <svg class="wave" viewBox="0 0 386 20" aria-hidden="true"><path d="M0 18 C120 16 260 8 386 4 L386 20 L0 20Z" fill="var(--white)"/></svg>
  <span class="logo-text" style="color:var(--navy)">Marrowind Labs</span>
  <span class="page-mark"></span>
</section>

</body>
</html>
```